Business Card Design for boarding house accomodation business

I need a business card design for my Sydney based boarding house business accomodation. providing rooms for rent in Sydney Australia with shard bathroom and kitchen.
The front of card, are my details with details of head office and the rear of card to have details of locations providing rooms for rent.

Industry/Entity Type

Business

Contact Information for Business Card

Front of card details:
HOLLINBROOK MANAGEMENT PTY LTD t/a
CALLOWAY'S GUEST HOUSE
ABN:52930718264
Daniel Vukasinov
48 Pembury st
Newtown 2042
Mobile:0412876390
Email:daniel@callowaysguesthouse-example.com.au

Back of Card:
Locations:
-48 Pembury st
Newtown 2042

-392 Carvel st
Erskineville 2043

-87 Whitlam st
Bondi 2026

-264 Ashcombe rd
Marrickville 2043

```html
<!DOCTYPE html>
<html lang="en">
<head>
<meta charset="utf-8">
<title>Calloway's Guest House – Business Card</title>
<link href="https://fonts.googleapis.com/css2?family=Cinzel:wght@400;600&family=Open+Sans:wght@400;600;700&display=swap" rel="stylesheet">
<style>
  :root{
    --orange:#d9520f;
    --ink:#3a3a3a;
    --rule:#bdbdbd;
    --paper:#ffffff;
    --backdrop:#ecebe8;
  }
  *{box-sizing:border-box;margin:0;padding:0}
  html,body{width:1200px;height:1024px;overflow:hidden}
  body{background:var(--backdrop);font-family:"Open Sans",Arial,sans-serif;color:var(--ink);position:relative}

  .card{position:absolute;left:250px;width:700px;height:400px;background:var(--paper);overflow:hidden;box-shadow:0 6px 20px rgba(0,0,0,.12)}
  .card--front{top:70px}
  .card--back{top:554px}

  /* Brand name placeholder: one font, one weight, one colour */
  .brand{display:flex;align-items:center;gap:12px}
  .brand__square{width:14px;height:14px;flex:none}
  .brand__name{font-family:"Open Sans",Arial,sans-serif;font-weight:600;line-height:1.25}

  /* FRONT */
  .front__band{position:absolute;left:0;right:0;bottom:0;height:26px;background:var(--orange)}
  .front__brand{position:absolute;left:40px;top:130px;width:270px;justify-content:center}
  .front__brand .brand__name{font-size:24px;color:var(--ink)}
  .front__brand .brand__square{background:var(--orange)}
  .front__divider{position:absolute;left:328px;top:40px;width:1px;height:300px;background:var(--rule)}
  .front__address{position:absolute;left:40px;top:268px;font-size:16px;line-height:1.6;display:flex;gap:12px}
  .front__address .abn{color:var(--orange);font-weight:700}
  .front__address .abn span{color:var(--ink);font-weight:400}
  .company-tag{position:absolute;right:36px;top:36px;background:var(--orange);color:#fff;font-size:13px;font-weight:600;padding:5px 12px;border-radius:3px}
  .person{position:absolute;left:352px;top:92px;width:320px}
  .person__name{font-family:"Cinzel",Georgia,serif;font-size:24px;font-weight:600;letter-spacing:1.5px;padding-bottom:12px;border-bottom:1px solid var(--rule)}
  .contact-list{list-style:none;margin-top:18px}
  .contact-list li{display:flex;align-items:center;gap:10px;font-size:13px;line-height:1;margin-bottom:16px;white-space:nowrap}
  .icon{width:16px;height:16px;flex:none}

  /* BACK */
  .back__panel{position:absolute;left:0;right:0;top:0;height:250px;background:var(--orange);display:flex;align-items:center;justify-content:center}
  .back__panel .brand__name{color:#fff;font-size:30px}
  .back__panel .brand__square{background:#fff}
  .back__band{position:absolute;left:0;right:0;bottom:0;height:150px;padding:20px 28px}
  .locations__title{font-family:"Cinzel",Georgia,serif;font-weight:600;font-size:18px;letter-spacing:2px;text-align:center}
  .locations{display:flex;justify-content:space-between;margin-top:20px}
  .location{font-size:14px;line-height:1.55;text-align:center;flex:1;position:relative}
  .location + .location::before{content:"";position:absolute;left:0;top:4px;width:2px;height:38px;background:var(--orange);transform:skewX(-20deg)}
</style>
</head>
<body>

<section class="card card--front" aria-label="Business card front">
  <div class="brand front__brand">
    <span class="brand__square" aria-hidden="true"></span>
    <p class="brand__name">CALLOWAY'S<br>GUEST HOUSE</p>
  </div>
  <div class="front__divider"></div>
  <div class="front__address">
    <svg class="icon" viewBox="0 0 16 16" aria-hidden="true"><path d="M8 1a5 5 0 0 0-5 5c0 4 5 9 5 9s5-5 5-9a5 5 0 0 0-5-5zm0 7a2 2 0 1 1 0-4 2 2 0 0 1 0 4z" fill="var(--orange)"/></svg>
    <p>48 Pembury st<br>Newtown 2042<br><span class="abn">ABN: <span>52930718264</span></span></p>
  </div>

  <p class="company-tag">Hollinbrook Management Pty Ltd</p>
  <div class="person">
    <h1 class="person__name">DANIEL VUKASINOV</h1>
    <ul class="contact-list">
      <li><svg class="icon" viewBox="0 0 16 16" aria-hidden="true"><rect x="4" y="1" width="8" height="14" rx="1.5" fill="none" stroke="var(--orange)" stroke-width="1.6"/><circle cx="8" cy="12.3" r=".9" fill="var(--orange)"/></svg>0412876390</li>
      <li><svg class="icon" viewBox="0 0 16 16" aria-hidden="true"><rect x="1" y="3" width="14" height="10" rx="1" fill="var(--orange)"/><path d="M1.5 3.5 8 9l6.5-5.5" fill="none" stroke="#fff" stroke-width="1.3"/></svg>daniel@callowaysguesthouse-example.com.au</li>
      <li><svg class="icon" viewBox="0 0 16 16" aria-hidden="true"><circle cx="8" cy="8" r="7" fill="var(--orange)"/><path d="M1 8h14M8 1c-3 3-3 11 0 14M8 1c3 3 3 11 0 14" fill="none" stroke="#fff" stroke-width="1"/></svg>www.callowaysguesthouse-example.com.au</li>
    </ul>
  </div>
  <div class="front__band"></div>
</section>

<section class="card card--back" aria-label="Business card back">
  <div class="back__panel">
    <div class="brand">
      <span class="brand__square" aria-hidden="true"></span>
      <p class="brand__name">CALLOWAY'S GUEST HOUSE</p>
    </div>
  </div>
  <div class="back__band">
    <h2 class="locations__title">OUR LOCATIONS</h2>
    <div class="locations">
      <p class="location">48 Pembury st<br>Newtown 2042</p>
      <p class="location">392 Carvel st<br>Erskineville 2043</p>
      <p class="location">87 Whitlam st<br>Bondi 2026</p>
      <p class="location">264 Ashcombe rd<br>Marrickville 2043</p>
    </div>
  </div>
</section>

</body>
</html>
```